I'm a family owned and operated electrical contractor in Colorado USA. We offer a full electrical service, remodel and new construction, we also offer energy saving solutions like LED lighting, photo voltaic, and wind energy,
We sell and install BrightNova light fixtures (rbightNova.com)
More information about my business can be looked at my website copperpeakelcetric.com My logo is on my website.

Industry/Entity Type

Electrical

Contact Information for Business Card

Copper Peak Electric, Dwight Sorensby, Owner, BrightNova Sale & Install, Full Electrical Service, Remodel & New Construction. P: 303-512-8847 F:303-264-3318 E:dwight@copperpeakelectric.com, 27519 CR41, Ashvale, MT 80194

```html
<!DOCTYPE html>
<html lang="en">
<head>
<meta charset="utf-8">
<title>Copper Peak Electric – Business Card</title>
<link href="https://fonts.googleapis.com/css2?family=Archivo:wght@700&family=Source+Sans+3:wght@400;700&family=PT+Sans+Narrow:wght@400;700&display=swap" rel="stylesheet">
<style>
  :root {
    --brand-green: #3db54a;
    --band-green: #5fbb46;
    --icon-green-light: #8fd16a;
    --ink-dark: #1e1e1e;
    --ink-grey: #5e5e5e;
    --paper: #ffffff;
    --paper-shade: #f1f1f1;
    --band-shadow: #d4d4d4;
  }
  * { margin: 0; padding: 0; box-sizing: border-box; }
  html, body { width: 1200px; height: 702px; overflow: hidden; background: var(--paper); }
  .card {
    position: relative;
    width: 1200px;
    height: 702px;
    overflow: hidden;
    background: linear-gradient(135deg, var(--paper) 0%, var(--paper-shade) 100%);
  }
  .company-name {
    position: absolute;
    left: 61px;
    top: 56px;
    font-family: "Archivo", sans-serif;
    font-weight: 700;
    font-size: 35px;
    letter-spacing: 1px;
    color: var(--ink-dark);
    text-transform: uppercase;
    white-space: nowrap;
  }
  .energy-icons {
    position: absolute;
    left: 61px;
    top: 135px;
    display: flex;
    gap: 20px;
  }
  .energy-icon {
    width: 100px;
    height: 100px;
    border-radius: 50%;
    background: radial-gradient(circle at 50% 35%, var(--icon-green-light) 0%, var(--brand-green) 75%);
  }
  .person {
    position: absolute;
    right: 59px;
    top: 184px;
    text-align: right;
    font-family: "Source Sans 3", sans-serif;
  }
  .person-name {
    font-weight: 700;
    font-size: 58px;
    line-height: 1;
    color: var(--brand-green);
    white-space: nowrap;
  }
  .person-title {
    margin-top: 6px;
    font-weight: 400;
    font-size: 42px;
    line-height: 1;
    color: var(--ink-grey);
  }
  .contact-list {
    position: absolute;
    left: 61px;
    top: 343px;
    list-style: none;
    font-family: "PT Sans Narrow", sans-serif;
    font-size: 33px;
    color: var(--ink-grey);
  }
  .contact-item {
    display: flex;
    align-items: center;
    height: 51px;
  }
  .contact-icon {
    width: 40px;
    height: 32px;
    margin-right: 15px;
    fill: var(--brand-green);
  }
  .address {
    position: absolute;
    right: 59px;
    top: 450px;
    font-family: "PT Sans Narrow", sans-serif;
    font-size: 33px;
    line-height: 40px;
    color: var(--ink-grey);
    white-space: nowrap;
  }
  .service-band {
    position: absolute;
    left: 0;
    top: 0;
    width: 1200px;
    height: 702px;
  }
  .services {
    position: absolute;
    left: 0;
    right: 0;
    top: 609px;
    text-align: center;
    font-family: "PT Sans Narrow", sans-serif;
    font-weight: 700;
    font-size: 35px;
    line-height: 42px;
    color: var(--paper);
    white-space: nowrap;
  }
  .services .divider { margin: 0 18px; }
</style>
</head>
<body>
<div class="card">
  <svg class="service-band" viewBox="0 0 1200 702" aria-hidden="true">
    <path d="M0 534 Q600 626 1200 534 L1200 702 L0 702 Z" fill="var(--band-shadow)"/>
    <path d="M0 541 Q600 632 1200 541 L1200 702 L0 702 Z" fill="var(--band-green)"/>
  </svg>

  <div class="company-name">Copper Peak Electric</div>
  <div class="energy-icons">
    <div class="energy-icon" role="img" aria-label="Green circle with sun icon"></div>
    <div class="energy-icon" role="img" aria-label="Green circle with wind turbine icon"></div>
    <div class="energy-icon" role="img" aria-label="Green circle with tree icon"></div>
    <div class="energy-icon" role="img" aria-label="Green circle with water drop icon"></div>
  </div>

  <div class="person">
    <div class="person-name">Dwight Sorensby</div>
    <div class="person-title">Owner</div>
  </div>

  <ul class="contact-list">
    <li class="contact-item">
      <svg class="contact-icon" viewBox="0 0 40 32" aria-label="Phone" role="img">
        <path d="M9 2 L14 2 L17 10 L13 13 C15 18 19 22 24 24 L27 20 L35 23 L35 28 C35 30 33 31 31 31 C17 30 7 20 6 6 C6 4 7 2 9 2 Z"/>
      </svg>
      <span>303-512-8847</span>
    </li>
    <li class="contact-item">
      <svg class="contact-icon" viewBox="0 0 40 32" aria-label="Fax" role="img">
        <rect x="11" y="1" width="18" height="11" rx="1"/>
        <rect x="4" y="13" width="32" height="10" rx="2"/>
        <rect x="9" y="21" width="22" height="10" rx="1"/>
        <rect x="12" y="24" width="16" height="2" fill="var(--paper)"/>
        <rect x="12" y="27.5" width="16" height="2" fill="var(--paper)"/>
      </svg>
      <span>303-264-3318</span>
    </li>
    <li class="contact-item">
      <svg class="contact-icon" viewBox="0 0 40 32" aria-label="Email" role="img">
        <path d="M2 8 L38 8 L20 19 Z"/>
        <path d="M2 11 L20 22 L38 11 L38 26 L2 26 Z"/>
      </svg>
      <span>dwight@copperpeakelectric.com</span>
    </li>
  </ul>

  <div class="address">27519 CR41, Ashvale, MT 80194</div>

  <div class="services">
    <span>BrightNova Sale &amp; Install</span><span class="divider">|</span><span>Full Electrical Service</span><span class="divider">|</span><span>Remodel &amp; New Construction</span>
  </div>
</div>
</body>
</html>
```